Email marketing template

Job type:
Email marketing

Task description:
We would like to send an E-card to our clients wishing them a Merry Christmas

Copy for email marketing:

Seasons Greetings from everyone at PRV…

This year we are supporting our chosen charities by making a donation to help them continue their hard work making a difference. Have a look at our website to find more about the chosen charities we are supporting this Christmas:

http://www.morvenhale.com/Our-Approach/Brightloom

Best wishes,

The PRV team

Logo text:
PRV

Descriptive words:
Fun
Playful
Bold
Festive

Deadline:
Monday 16th December

Other information:
We will require you to provide us with HTML coding and uploading to Mail Chimp. We will then process payment upon testing final materials.

Industry/Entity Type

Marketing

```html
<!DOCTYPE html>
<html lang="en">
<head>
<meta charset="utf-8">
<title>Season's Greetings from everyone at PRV</title>
<link rel="stylesheet" href="https://fonts.googleapis.com/css2?family=Alfa+Slab+One&family=Arimo:wght@400;700&family=Playfair+Display:wght@400;700&display=swap">
<style>
  :root {
    --paper: #ffffff;
    --teal: #7dc1bf;
    --teal-dark: #2f5e68;
    --navy: #2b4468;
    --ink: #1f2d5c;
    --red: #d4515f;
    --gold: #c8a86b;
    --brown: #8a6d3b;
    --link: #3a8fd0;
    --muted: #555555;
  }
  html, body {
    margin: 0;
    padding: 0;
    width: 880px;
    height: 1200px;
    overflow: hidden;
    background: var(--paper);
  }
  .ecard {
    position: relative;
    width: 880px;
    height: 1200px;
    overflow: hidden;
    background: var(--paper);
    font-family: "Arimo", Arial, sans-serif;
    color: var(--ink);
  }
  .preheader {
    position: absolute;
    top: 14px;
    left: 0;
    width: 880px;
    text-align: center;
    font-size: 17px;
    line-height: 25px;
    color: var(--brown);
    z-index: 2;
  }
  .preheader a {
    color: var(--brown);
    font-weight: 700;
  }
  .hero-art {
    position: absolute;
    left: 0;
    top: 0;
  }
  .sleigh {
    position: absolute;
    left: 268px;
    top: 196px;
    width: 92px;
    height: 56px;
    border-radius: 22px;
    background: linear-gradient(160deg, #e07a85, var(--red));
  }
  .reindeer-team {
    position: absolute;
    left: 380px;
    top: 150px;
    width: 180px;
    height: 62px;
    border-radius: 22px;
    background: linear-gradient(90deg, var(--red), #e07a85);
  }
  .headline {
    position: absolute;
    left: 0;
    top: 240px;
  }
  .headline text {
    font-family: "Alfa Slab One", Georgia, serif;
    fill: var(--teal);
    stroke: var(--navy);
    stroke-width: 4px;
    paint-order: stroke;
  }
  .headline g {
    filter: drop-shadow(4px 5px 0 var(--navy));
  }
  .from-line {
    position: absolute;
    top: 550px;
    left: 84px;
    display: flex;
    align-items: center;
    gap: 18px;
    font-family: "Playfair Display", Georgia, serif;
    font-size: 40px;
    letter-spacing: 3px;
    color: var(--navy);
    white-space: nowrap;
  }
  .brand {
    display: flex;
    align-items: center;
    gap: 10px;
  }
  .brand-mark {
    width: 30px;
    height: 30px;
    background: var(--teal);
  }
  .holly {
    position: absolute;
    left: 476px;
    top: 660px;
    width: 76px;
    height: 68px;
    border-radius: 50%;
    background: radial-gradient(circle at 40% 65%, rgba(212,81,95,0.85), rgba(125,193,191,0.8));
  }
  .message {
    position: absolute;
    top: 754px;
    left: 60px;
    width: 760px;
    text-align: center;
    font-size: 22px;
    line-height: 24px;
    color: var(--ink);
  }
  .message p {
    margin: 0 0 27px;
  }
  .message a {
    color: var(--link);
  }
  .contact-icons {
    position: absolute;
    top: 1004px;
    left: 198px;
    display: flex;
    gap: 23px;
  }
  .contact-icon {
    width: 80px;
    height: 80px;
    border-radius: 10px;
    background: var(--teal);
    display: flex;
    align-items: center;
    justify-content: center;
  }
  .contact-icon svg {
    width: 52px;
    height: 52px;
    fill: none;
    stroke: var(--teal-dark);
    stroke-width: 2.4;
    stroke-linejoin: round;
    stroke-linecap: round;
  }
  .footer {
    position: absolute;
    top: 1129px;
    left: 0;
    width: 880px;
    text-align: center;
    font-size: 16px;
    line-height: 24px;
    color: var(--muted);
  }
</style>
</head>
<body>
<main class="ecard">

  <div class="preheader">
    Get paid to take part in market researchEmail not displaying correctly?<br>
    <a href="#">View it in your browser</a>.
  </div>

  <svg class="hero-art" width="880" height="760" viewBox="0 0 880 760" aria-hidden="true">
    <circle class="moon" cx="483" cy="182" r="102" fill="var(--gold)"/>
    <line x1="78" y1="510" x2="804" y2="510" stroke="var(--red)" stroke-width="4"/>
    <line x1="78" y1="626" x2="804" y2="626" stroke="var(--red)" stroke-width="4"/>
    <g class="year-ribbon">
      <polygon points="356,672 478,672 468,692 478,712 356,712 366,692" fill="var(--navy)"/>
      <text x="418" y="702" text-anchor="middle" fill="#ffffff"
            font-family="'Playfair Display', Georgia, serif" font-weight="700" font-size="27">2014</text>
    </g>
  </svg>

  <div class="sleigh" role="img" aria-label="Santa in his sleigh"></div>
  <div class="reindeer-team" role="img" aria-label="Two reindeer pulling the sleigh across the moon"></div>

  <svg class="headline" width="880" height="260" viewBox="0 0 880 260">
    <g>
      <text x="231" y="113" font-size="116" textLength="432" lengthAdjust="spacingAndGlyphs">SEASON’S</text>
      <text x="106" y="240" font-size="158" textLength="694" lengthAdjust="spacingAndGlyphs">GREETINGS</text>
    </g>
  </svg>

  <div class="from-line">
    <span>FROM EVERYONE AT</span>
    <span class="brand"><span class="brand-mark"></span>PRV</span>
  </div>

  <div class="holly" role="img" aria-label="Sprig of holly with red berries"></div>

  <section class="message">
    <p>This year we are supporting our chosen charities by making a<br>donation to help them continue their hard work making a difference.</p>
    <p>Have a <a href="http://www.morvenhale.com/Our-Approach/Brightloom">look at our website</a> to find more about the chosen charities<br>we are supporting this Christmas.</p>
    <p class="signoff">Best wishes,<br>The PRV team</p>
  </section>

  <nav class="contact-icons">
    <a class="contact-icon" href="#" aria-label="Phone">
      <svg viewBox="0 0 52 52"><rect x="16" y="6" width="20" height="40" rx="3"/><line x1="16" y1="13" x2="36" y2="13"/><line x1="16" y1="38" x2="36" y2="38"/><circle cx="26" cy="42" r="1.5"/></svg>
    </a>
    <a class="contact-icon" href="#" aria-label="Email">
      <svg viewBox="0 0 52 52"><rect x="6" y="13" width="40" height="27" rx="2"/><polyline points="6,13 26,30 46,13"/><line x1="6" y1="40" x2="21" y2="26"/><line x1="46" y1="40" x2="31" y2="26"/></svg>
    </a>
    <a class="contact-icon" href="#" aria-label="Write to us">
      <svg viewBox="0 0 52 52"><polygon points="36,8 44,16 18,42 8,44 10,34"/><line x1="31" y1="13" x2="39" y2="21"/><line x1="10" y1="34" x2="18" y2="42"/></svg>
    </a>
    <a class="contact-icon" href="#" aria-label="Our team">
      <svg viewBox="0 0 52 52"><circle cx="24" cy="18" r="9"/><path d="M8 44c0-9 7-15 16-15s16 6 16 15z"/><path d="M34 11a8 8 0 0 1 0 15"/><path d="M38 30c5 2 8 7 8 14"/></svg>
    </a>
    <a class="contact-icon" href="#" aria-label="Chat">
      <svg viewBox="0 0 52 52"><path d="M6 10h28v18H18l-7 6v-6H6z"/><path d="M34 18h12v18h-5v6l-7-6H20v-8"/><circle cx="14" cy="19" r="1"/><circle cx="20" cy="19" r="1"/><circle cx="26" cy="19" r="1"/></svg>
    </a>
  </nav>

  <footer class="footer">
    No longer wish to receive these emails? Unsubscribe.<br>
    Copyright © 2013 PRV. All rights reserved.
  </footer>

</main>
</body>
</html>
```